Business Card Needed for Crafter of Pottery, Jewelry and Artwork

Calling all designers in search of an artistic challenge.

I need a new business card design for my pottery, jewelry and artwork business, Woven Glass and Tide, based in Vancouver BC.

I would like a card that is bright and inviting and preferably incorporates my logo and a sample of photos of my work while having a clean fresh look. The following contact details would preferably be included on the card as well:
• Helena Pikeworth
• Designer
• Phone: 604.555.0172
• Email: Designer@WovenGlassandTide.example
• Website: www.WovenGlassandTide.example
• Blog: www.ShapingHillside.example

The logo is attached in two color schemes in both Vector and Source formats. On past cards I’ve also included photos of my work. By including photos of the work the pieces are showcased and it catches people’s eye and prompts them to pick up the card and look at it more closely. For example, if I leave a stack in a coffee shop I want people to be drawn to the card, to pick it up and get a sense of the my product lines. Please feel free to pull photos of my work directly off of my website. If you need photos with higher pixels please let me know and I’ll email them directly to you. The website background is bffbda (191, 251, 218). I would like the business cards to match the feel of the website for consistency but the cards do not need to use the exact same colors. My website and current business card are predominantly turquoise shades. The background uses stripes provided by the website template. I don’t know the exact colors of the stripes.

My current business card is attached to show the use of photos in a design. Please note that I am not thrilled with my own design and am looking for variations and completely new designs. This example is not meant to be used as a template or starting point.

Here is some background surrounding my company:
WGT offers one of a kind jewelry, pottery, artwork and leather bags each designed with a twist. The pottery varies from rustic every day functional ware to raku artwork. The jewelry ranges from simple sterling every day pieces to multimedia pieces incorporating stone, metal, ceramics and fabric. The artwork is multimedia, typically acrylic paired with a natural element such as bark. All the bags are leather with reworked kimono fabric or patterned silk lining.

Feel free to check out my website to get a flavour for my work and the color scheme I've used on marketing materials so far. www.wovenglassandtide.example
Updates

Thank you to everyone who has submitted a design so far. I hope everyone has received some helpful feedback.

I'm going to post a survey to customers and friends asking for their votes. If you have new designs to submit please try to get them in by Saturday March 30 at noon so that I can include it in the survey launch.

Thank you

Target Market(s)

Females aged 25-65 interested in one of a kind functional pottery and jewelry.

Industry/Entity Type

Coffee Shop

Requirements
Must have
• Contact information, website, blog
Nice to have
• Logo, photos

```html
<!DOCTYPE html>
<html lang="en">
<head>
<meta charset="utf-8">
<title>Woven Glass and Tide — Business Card</title>
<link rel="stylesheet" href="https://fonts.googleapis.com/css2?family=EB+Garamond:ital,wght@0,400;0,700;1,400&display=swap">
<style>
  :root {
    --canvas: #ecebe7;
    --card: #ffffff;
    --mint: #cdeee7;
    --navy: #2b2f86;
    --teal: #1ea895;
    --pot-brown: #8a5a3a;
    --pot-green: #4fb89a;
    --bag-teal: #2bb3c0;
    --bag-grey: #8e9599;
    --shadow: rgba(0, 0, 0, 0.22);
  }
  * { box-sizing: border-box; margin: 0; padding: 0; }
  html, body { width: 1200px; height: 1000px; overflow: hidden; }
  body {
    background: var(--canvas);
    font-family: "EB Garamond", Georgia, serif;
    position: relative;
  }
  .card {
    position: absolute;
    left: 320px;
    width: 560px;
    height: 320px;
    background: var(--card);
    box-shadow: 0 6px 18px var(--shadow);
    overflow: hidden;
  }
  .card--front { top: 140px; }
  .card--back { top: 540px; }

  /* Front */
  .front__band {
    position: absolute; left: 0; top: 0; width: 100%; height: 190px;
    background: var(--mint);
  }
  .photo { position: absolute; }
  .photo--pots {
    left: 40px; top: 62px; width: 140px; height: 84px;
    background: linear-gradient(180deg, var(--pot-brown) 0%, var(--pot-brown) 45%, var(--pot-green) 60%, #3a3a3a 100%);
  }
  .photo--bag {
    right: 40px; top: 100px; width: 140px; height: 66px;
    background: linear-gradient(135deg, var(--bag-grey) 0%, var(--bag-grey) 45%, var(--bag-teal) 55%, var(--bag-teal) 100%);
  }
  .front__mark {
    position: absolute; left: 205px; top: 40px; width: 150px; height: 150px;
    display: flex; align-items: center; justify-content: center;
  }
  .front__mark svg { position: absolute; inset: 0; }
  .front__mark-name {
    position: relative; width: 110px; text-align: center;
    color: var(--navy); font-weight: 700; font-size: 17px; line-height: 1.1;
  }
  .front__title {
    position: absolute; left: 0; right: 0; top: 215px;
    text-align: center; color: var(--navy); font-weight: 700; font-size: 28px;
  }

  /* Back */
  .back__mark {
    position: absolute; left: 30px; top: 26px;
    display: flex; align-items: center; gap: 10px;
  }
  .back__mark-name {
    color: var(--navy); font-weight: 700; font-size: 18px; line-height: 1.05; width: 100px;
  }
  .back__person { position: absolute; left: 200px; top: 62px; }
  .back__name { color: var(--navy); font-weight: 700; font-size: 21px; line-height: 1.1; }
  .back__role { color: var(--navy); font-weight: 700; font-size: 16px; opacity: .85; }
  .contact-list {
    position: absolute; left: 40px; top: 150px; list-style: none;
    font-size: 17px; line-height: 1.45;
  }
  .contact-list li { display: flex; gap: 8px; }
  .contact-list .label { color: var(--navy); font-style: italic; width: 18px; text-align: right; }
  .contact-list .value { color: var(--teal); }
  .photo--jar {
    right: 40px; bottom: 20px; width: 105px; height: 105px; border-radius: 12px;
    background: linear-gradient(180deg, #a9825e 0%, #8a5a3a 45%, #bfe6dc 70%, #e8f5f1 100%);
  }
</style>
</head>
<body>
  <section class="card card--front" aria-label="Card front">
    <div class="front__band"></div>
    <div class="photo photo--pots" role="img" aria-label="Photo of two glazed pottery cups in brown and green"></div>
    <div class="front__mark">
      <svg viewBox="0 0 150 150" aria-hidden="true"><circle cx="75" cy="75" r="72" fill="#ffffff" opacity=".55" stroke="var(--teal)" stroke-width="2"/></svg>
      <span class="front__mark-name">Woven Glass and Tide</span>
    </div>
    <div class="photo photo--bag" role="img" aria-label="Photo of a teal and grey leather clutch bag"></div>
    <h1 class="front__title">Woven Glass and Tide</h1>
  </section>

  <section class="card card--back" aria-label="Card back">
    <div class="back__mark">
      <svg width="28" height="28" viewBox="0 0 28 28" aria-hidden="true"><circle cx="14" cy="14" r="12" fill="none" stroke="var(--teal)" stroke-width="3"/></svg>
      <span class="back__mark-name">Woven Glass and Tide</span>
    </div>
    <div class="back__person">
      <p class="back__name">Helena Pikeworth</p>
      <p class="back__role">Designer</p>
    </div>
    <ul class="contact-list">
      <li><span class="label">P:</span><span class="value">604.555.0172</span></li>
      <li><span class="label">E:</span><span class="value">Designer@WovenGlassandTide.example</span></li>
      <li><span class="label">W:</span><span class="value">www.WovenGlassandTide.example</span></li>
      <li><span class="label">B:</span><span class="value">www.ShapingHillside.example</span></li>
    </ul>
    <div class="photo photo--jar" role="img" aria-label="Photo of a brown and mint glazed pottery jar"></div>
  </section>
</body>
</html>
```